Christian author needs a book cover design.

I am looking to find a cover design for my new book—A Lantern at Dawn, Quiet Harbor: Herald, Keeper, and Warden. The finished work should be a jpg format file. The finished book cover is 6” by 9” so I need the image size to be 12.87” wide by 9” high with an included spine section of 0.87” and a bleed of 0.125”.
The front should include the following in relatively small text:
“A Lantern at Dawn” and “Delia Brannock-Suvé” (as author)
It should also include the text “Quiet Harbor” in a medium size.
The phrase “Herald, Keeper, and Warden” should be a large size and visually dominant. Along with these text/word art items, I want images of a scroll, a menorah with a star of David, and a crown with a cross. If your vision of the cover includes working the images into the “Herald (scroll), Keeper (menorah), and Warden (crown)” text art, please associate the words and images as indicated. Also I would like for the primary color of the cover to be a dark, scarlet red. Thank you!

Industry/Entity Type

Christian

Requirements
Must have
• A winning design must have copyright printing permissions for all elements. Minimally altered web grab images won't work.

```html
<!DOCTYPE html>
<html lang="en">
<head>
<meta charset="utf-8">
<title>A Lantern at Dawn, Quiet Harbor: Herald, Keeper, and Warden — Book Cover</title>
<link rel="stylesheet" href="https://fonts.googleapis.com/css2?family=Bebas+Neue&family=Playwrite+FR+Trad:wght@300&display=swap">
<style>
  :root {
    --page: #ffffff;
    --scarlet: #9b0b0f;
    --ink-light: #ffffff;
    --crown-gold: #ffe600;
    --display-font: "Bebas Neue", "Oswald", sans-serif;
    --script-font: "Playwrite FR Trad", "Dancing Script", cursive;
  }
  html, body {
    margin: 0;
    padding: 0;
    width: 1200px;
    height: 1000px;
    overflow: hidden;
    background: var(--page);
  }
  .cover-canvas {
    display: block;
    width: 1200px;
    height: 1000px;
  }
  .cover-panel { fill: var(--scarlet); }
  .title-display {
    font-family: var(--display-font);
    fill: var(--ink-light);
    text-anchor: middle;
    font-size: 112px;
  }
  .subtitle-display {
    font-family: var(--display-font);
    fill: var(--ink-light);
    font-size: 68px;
  }
  .subtitle-left { text-anchor: start; }
  .subtitle-right { text-anchor: end; }
  .script-line {
    font-family: var(--script-font);
    font-weight: 300;
    fill: var(--ink-light);
    text-anchor: middle;
  }
  .emblem-light { fill: var(--ink-light); }
  .emblem-gold { fill: var(--crown-gold); }
</style>
</head>
<body>
<svg class="cover-canvas" viewBox="0 0 1200 1000" xmlns="http://www.w3.org/2000/svg">
  <rect class="cover-panel" x="270" y="0" width="667" height="1000"/>

  <text class="script-line series-line" x="603" y="64" font-size="34">A Lantern at Dawn</text>

  <text class="subtitle-display subtitle-left" x="418" y="128">QUIET</text>
  <text class="subtitle-display subtitle-right" x="780" y="128">HARBOR</text>

  <g class="emblem emblem-scroll" role="img" aria-label="Hand-drawn white scroll, emblem of the Herald">
    <rect class="emblem-light" x="524" y="138" width="128" height="128" rx="28"/>
  </g>

  <text class="title-display role-herald" x="596" y="378">HERALD</text>

  <g class="emblem emblem-menorah" role="img" aria-label="Hand-drawn white menorah topped with a star of David, emblem of the Keeper">
    <rect class="emblem-light" x="498" y="402" width="186" height="163" rx="24"/>
  </g>

  <text class="title-display role-keeper" x="600" y="654">KEEPER</text>

  <g class="emblem emblem-crown" role="img" aria-label="Hand-drawn yellow crown with a cross, emblem of the Warden">
    <rect class="emblem-gold" x="520" y="668" width="160" height="136" rx="20"/>
  </g>

  <text class="title-display role-warden" x="600" y="890">WARDEN</text>

  <text class="script-line author-name" x="601" y="970" font-size="30">Delia Brannock-Suvé</text>
</svg>
</body>
</html>
```